Documentary Movie Needs a Poster

We need a poster/lobby card for a documentary film made by six filmmakers. Lobby card needs to list name of sponsor, names of filmmakers and (if feasible, but not required) image frames from each of the six sections of the film.

Text should be very readable. OK to have all caps text or upper/lower.

Design comps are OK, these do not need to be print-ready final images.

Target Market(s)

well educated documentary filmgoers

Industry/Entity Type

Movie

Requirements
Must have
• Must contain the following text (please use helvetica neue or similar font).

Please use the following sponsor name:

The
Harwell Center for Filmmaking
presents

Please use the following filmmaker names:

Theodore Marsouli
Patrick Ennis
Raymond Hollowell
Samuel R. T. Vorne
Oliver Prescott
Danny Rusk

Please use the 6 images in archive/zip to create the card.

You can also do text-only versions of the card (no images).

Card needs to be 2:1 aspect ratio (2000px wide x 1000 pixels high)

Names of filmmakers should each be same size (no filmmaker has visual priority over the other).

Colors for text, lines and other design elements should be RED, BLACK and/or WHITE.

Feel free to crop images if you need to.

```html
<!DOCTYPE html>
<html lang="en">
<head>
<meta charset="utf-8">
<title>Harwell Center for Filmmaking Presents</title>
<link href="https://fonts.googleapis.com/css2?family=Arimo:ital,wght@0,400;0,700;1,400&display=swap" rel="stylesheet">
<style>
  :root {
    --black: #000000;
    --white: #ffffff;
    --red: #c71f2d;
    --gap: #ffffff;
  }
  * { margin: 0; padding: 0; box-sizing: border-box; }
  html, body {
    width: 1200px;
    height: 600px;
    overflow: hidden;
    background: var(--black);
  }
  .card {
    position: relative;
    width: 1200px;
    height: 600px;
    display: flex;
    font-family: "Arimo", "Helvetica Neue", Helvetica, Arial, sans-serif;
  }
  .credits {
    width: 524px;
    height: 600px;
    background: var(--black);
    padding: 32px 0 0 24px;
  }
  .sponsor {
    display: flex;
    align-items: flex-start;
    gap: 14px;
  }
  .sponsor-mark {
    flex: none;
    width: 18px;
    height: 18px;
    margin-top: 16px;
    background: var(--red);
  }
  .sponsor-name {
    color: var(--white);
    font-weight: 400;
    font-size: 44px;
    line-height: 52px;
    letter-spacing: -0.3px;
  }
  .divider {
    margin-top: 30px;
    width: 284px;
    height: 4px;
    background: var(--red);
    border: 0;
  }
  .presents {
    margin-top: 22px;
    color: var(--white);
    font-style: italic;
    font-size: 25px;
    letter-spacing: 0.5px;
    text-transform: uppercase;
  }
  .filmmakers {
    list-style: none;
    margin-top: 22px;
    color: var(--white);
    text-transform: uppercase;
    font-size: 33px;
    line-height: 47.6px;
    letter-spacing: -0.3px;
  }
  .filmmakers .first { font-weight: 400; }
  .filmmakers .last { font-weight: 700; }
  .frames {
    flex: 1;
    display: grid;
    grid-template-columns: 1fr 1fr;
    grid-template-rows: repeat(3, 1fr);
    gap: 3px;
    background: var(--gap);
    padding-left: 2px;
  }
  .frame { width: 100%; height: 100%; }
  .frame-desert { background: linear-gradient(180deg, #d8d0c0 0%, #b59f80 60%, #a48c6c 100%); }
  .frame-archive { background: linear-gradient(160deg, #c9c9c9 0%, #8a8a8a 55%, #4a4a4a 100%); }
  .frame-rooftop { background: linear-gradient(180deg, #9fb2c2 0%, #b8a486 45%, #8c7558 100%); }
  .frame-protest { background: linear-gradient(180deg, #6f93c8 0%, #a8b4c2 45%, #4a4a4e 100%); }
  .frame-militia { background: linear-gradient(180deg, #c9d3de 0%, #9c8470 50%, #5e5a48 100%); }
  .frame-roadside { background: linear-gradient(180deg, #c4c8cc 0%, #9ea19b 50%, #7c7560 100%); }
</style>
</head>
<body>
<main class="card">
  <section class="credits">
    <div class="sponsor">
      <span class="sponsor-mark" aria-hidden="true"></span>
      <h1 class="sponsor-name">The Harwell<br>Center for<br>Filmmaking</h1>
    </div>
    <hr class="divider">
    <p class="presents">Presents</p>
    <ul class="filmmakers">
      <li><span class="first">Theodore</span> <span class="last">Marsouli</span></li>
      <li><span class="first">Patrick</span> <span class="last">Ennis</span></li>
      <li><span class="first">Raymond</span> <span class="last">Hollowell</span></li>
      <li><span class="first">Samuel</span> <span class="last">R. T. Vorne</span></li>
      <li><span class="first">Oliver</span> <span class="last">Prescott</span></li>
      <li><span class="first">Danny</span> <span class="last">Rusk</span></li>
    </ul>
  </section>
  <section class="frames">
    <div class="frame frame-desert" role="img" aria-label="Film still: a destroyed armored vehicle half buried in desert sand"></div>
    <div class="frame frame-archive" role="img" aria-label="Black and white archival film still: a soldier resting among battlefield debris"></div>
    <div class="frame frame-rooftop" role="img" aria-label="Film still: soldiers aiming from a rooftop over a city with a minaret and rising smoke"></div>
    <div class="frame frame-protest" role="img" aria-label="Film still: anti-war protesters with signs in front of a domed capitol building"></div>
    <div class="frame frame-militia" role="img" aria-label="Film still: a crowd of armed fighters raising rifles"></div>
    <div class="frame frame-roadside" role="img" aria-label="Film still: a kneeling soldier with a rifle beside a highway"></div>
  </section>
</main>
</body>
</html>
```